Stage Show Poster - Beneath Copper Hills.

We are looking for an eye catching A3 poster to advertise our upcoming production ‘Beneath Copper Hills’. Please see the two attached files for all the information about the show and what we need on the poster.
The Synopsis file is provided to give you an idea of the production its not ment to be on the poster.

Target Market(s)

General Public western english speaking

Requirements
Must have
• See Poster Requirements File. A3 Portrait Poster.
Should not have
• Pictures of any prevous casts from the show or film.

```html
<!DOCTYPE html>
<html lang="en">
<head>
<meta charset="utf-8">
<title>Beneath Copper Hills – Stage Show Poster</title>
<link href="https://fonts.googleapis.com/css2?family=Great+Vibes&family=Lato:wght@400;700&display=swap" rel="stylesheet">
<style>
  :root {
    --brick-dark: #2a1a14;
    --brick-mid: #5a3a2c;
    --brick-light: #7a5443;
    --panel: #000000;
    --wood-deep: #3a0a06;
    --wood-warm: #7a1c10;
    --wood-glow: #a8351c;
    --text: #ffffff;
    --label: #d8322a;
    --badge-ring: #b9a3d6;
    --badge-fill: #6a3aa0;
    --button-top: #f4f6fb;
    --button-bar: #1f4fa8;
  }
  html, body {
    margin: 0;
    padding: 0;
    width: 1200px;
    height: 900px;
    overflow: hidden;
    background: var(--panel);
  }
  .poster {
    position: relative;
    width: 1200px;
    height: 900px;
    font-family: 'Lato', 'Gill Sans', sans-serif;
    color: var(--text);
    overflow: hidden;
  }
  .wall {
    position: absolute;
    top: 0;
    width: 280px;
    height: 900px;
    background: radial-gradient(ellipse at 50% 40%, var(--brick-light) 0%, var(--brick-mid) 45%, var(--brick-dark) 100%);
  }
  .wall--left { left: 0; }
  .wall--right { right: 0; width: 280px; }
  .stage {
    position: absolute;
    left: 280px;
    top: 0;
    width: 640px;
    height: 900px;
    background: var(--panel);
  }
  .instrument {
    position: absolute;
    left: 60px;
    top: 110px;
    width: 540px;
    height: 790px;
    background:
      radial-gradient(ellipse 38% 30% at 42% 42%, var(--wood-glow) 0%, var(--wood-warm) 40%, transparent 75%),
      radial-gradient(ellipse 45% 32% at 45% 82%, var(--wood-warm) 0%, var(--wood-deep) 55%, transparent 85%);
  }
  .content {
    position: absolute;
    inset: 0;
    text-align: center;
  }
  .producer {
    position: absolute;
    top: 26px;
    left: 0;
    right: 0;
    display: flex;
    justify-content: center;
    align-items: center;
    gap: 10px;
  }
  .producer__dot {
    width: 22px;
    height: 22px;
    border-radius: 50%;
    background: var(--badge-fill);
    border: 2px solid var(--badge-ring);
  }
  .producer__name {
    font-size: 30px;
    font-weight: 700;
    color: var(--text);
  }
  .presents {
    position: absolute;
    top: 118px;
    left: 0; right: 0;
    margin: 0;
    font-size: 30px;
    font-weight: 400;
  }
  .title {
    position: absolute;
    top: 182px;
    left: 0; right: 0;
    margin: 0;
    font-family: 'Great Vibes', cursive;
    font-weight: 400;
    font-size: 72px;
    line-height: 1;
  }
  .schedule {
    position: absolute;
    top: 300px;
    left: 0; right: 0;
    margin: 0;
    font-size: 25px;
    line-height: 32px;
  }
  .credits {
    position: absolute;
    top: 428px;
    left: 0; right: 0;
    margin: 0;
    font-size: 16px;
    line-height: 23px;
    text-transform: none;
  }
  .credits__label { color: var(--label); }
  .tickets {
    position: absolute;
    top: 596px;
    left: 0; right: 0;
    margin: 0;
    font-size: 26px;
  }
  .booking {
    position: absolute;
    top: 646px;
    left: 216px;
    width: 244px;
    height: 36px;
    border: 2px solid #c9d2e6;
    box-sizing: border-box;
    background: var(--button-top);
    color: #111;
    display: flex;
    flex-direction: column;
  }
  .booking__url {
    flex: 1;
    font-size: 13px;
    line-height: 20px;
  }
  .booking__label {
    background: var(--button-bar);
    color: var(--text);
    font-size: 8px;
    font-weight: 700;
    line-height: 12px;
  }
  .licence {
    position: absolute;
    top: 844px;
    left: 40px; right: 40px;
    margin: 0;
    font-size: 13px;
    line-height: 20px;
  }
</style>
</head>
<body>
<main class="poster">
  <div class="wall wall--left" role="img" aria-label="Photograph of an old red brick wall"></div>
  <div class="wall wall--right" role="img" aria-label="Photograph of an old red brick wall"></div>

  <section class="stage">
    <div class="instrument" role="img" aria-label="Close-up photograph of a violin body and strings lit in warm red"></div>

    <div class="content">
      <div class="producer">
        <span class="producer__dot"></span>
        <span class="producer__name">Lantern</span>
      </div>
      <p class="presents">presents</p>
      <h1 class="title">Beneath Copper Hills</h1>

      <p class="schedule">
        Ashbourne Town Hall<br>
        7:30pm on 15th to 16th November '12<br>
        2:30 pm &amp; 7:30pm on17th November '12
      </p>

      <p class="credits">
        <span class="credits__label">Music</span> EDWIN HALLORAN<br>
        <span class="credits__label">Lyrics</span> WALTER BRISCOE III<br>
        <span class="credits__label">Book</span> GERALD PRESCOTT and MARTIN OAKLEY<br>
        <span class="credits__label">Suggested by</span> "The Copperfield Choir" by Helena Marsh Copperfield
      </p>

      <p class="tickets">Tickets Available at</p>
      <div class="booking">
        <span class="booking__url">www.ashbourneboxoffice.co.uk</span>
        <span class="booking__label">Online Booking</span>
      </div>

      <p class="licence">
        This amateur production is presented by arrangement with HARLOW<br>
        MEREDITH LTD. on behalf of Crestline Theatricals of New York.
      </p>
    </div>
  </section>
</main>
</body>
</html>
```